Velmora Biz Card 2019

New business card for Velmora Property Inspections. We are a residential home inspection company in Arizona.

Target Market(s)

Real Estate

Font styles to use
Sans Serif

Requirements
Must have
• Glen Mirewick
• Home Inspector
• Velmora Property Inspections, LLC
• 480-555-0172
• glen@velmora-llc.example

```html
<!DOCTYPE html>
<html lang="en">
<head>
<meta charset="UTF-8">
<title>Velmora Biz Card 2019</title>
<link href="https://fonts.googleapis.com/css2?family=Lato:wght@400;700;900&display=swap" rel="stylesheet">
<style>
  :root {
    --page-bg: #e4e4e4;
    --card-dark: #6b6c70;
    --card-light: #f4f5f6;
    --brand-green: #3db843;
    --wordmark-light: #e6e6e8;
    --text-grey: #5a5b5e;
    --photo-top: #f2f3f4;
    --photo-mid: #c9b2a2;
    --photo-bottom: #1f2a44;
  }
  * { margin: 0; padding: 0; box-sizing: border-box; }
  html, body {
    width: 1200px;
    height: 1200px;
    overflow: hidden;
    background: var(--page-bg);
    font-family: "Lato", Arial, sans-serif;
  }
  .sheet {
    position: relative;
    width: 1200px;
    height: 1200px;
  }
  .card {
    position: absolute;
    left: 246px;
    width: 708px;
    height: 404px;
    overflow: hidden;
  }
  .card-front {
    top: 152px;
    background: var(--card-dark);
    display: flex;
    align-items: center;
    justify-content: center;
  }
  .front-brand {
    display: flex;
    align-items: center;
    gap: 18px;
  }
  .brand-dot {
    width: 34px;
    height: 34px;
    border-radius: 50%;
    background: var(--brand-green);
  }
  .front-wordmark {
    font-weight: 900;
    font-size: 46px;
    letter-spacing: 3px;
    color: var(--wordmark-light);
  }
  .card-back {
    top: 592px;
    background: var(--card-light);
  }
  .back-brand {
    position: absolute;
    left: 39px;
    top: 104px;
    display: flex;
    align-items: center;
    gap: 10px;
  }
  .back-brand .brand-dot {
    width: 18px;
    height: 18px;
  }
  .back-wordmark {
    font-weight: 900;
    font-size: 22px;
    letter-spacing: 1.5px;
    color: var(--text-grey);
  }
  .contact {
    position: absolute;
    left: 38px;
    top: 168px;
    color: var(--text-grey);
  }
  .person-name {
    font-size: 22px;
    font-weight: 700;
    color: var(--brand-green);
    line-height: 28px;
  }
  .person-role {
    font-size: 16px;
    line-height: 20px;
  }
  .company-name {
    margin-top: 18px;
    font-size: 16px;
    color: var(--brand-green);
    line-height: 20px;
  }
  .address {
    margin-top: 4px;
    font-size: 16px;
    line-height: 23px;
    font-style: normal;
  }
  .contact-lines {
    margin-top: 14px;
    list-style: none;
    font-size: 16px;
    line-height: 24px;
  }
  .contact-lines li {
    display: flex;
    align-items: center;
    gap: 7px;
  }
  .contact-lines svg { flex: none; }
  .portrait {
    position: absolute;
    left: 359px;
    top: 0;
    width: 349px;
    height: 404px;
    background: linear-gradient(180deg, var(--photo-top) 0%, var(--photo-mid) 45%, var(--photo-bottom) 72%, var(--photo-bottom) 100%);
  }
</style>
</head>
<body>
<main class="sheet">
  <section class="card card-front" aria-label="Card front">
    <div class="front-brand">
      <span class="brand-dot"></span>
      <span class="front-wordmark">VELMORA</span>
    </div>
  </section>

  <section class="card card-back" aria-label="Card back">
    <div class="back-brand">
      <span class="brand-dot"></span>
      <span class="back-wordmark">VELMORA</span>
    </div>

    <div class="contact">
      <h1 class="person-name">Glen Mirewick</h1>
      <p class="person-role">Home Inspector</p>
      <p class="company-name">Velmora Property Inspections, LLC</p>
      <address class="address">4410 S. Mesa Ridge Rd.<br>Tempe, AZ 85201</address>
      <ul class="contact-lines">
        <li>
          <svg width="12" height="12" viewBox="0 0 24 24" aria-hidden="true"><path fill="#3db843" d="M6.6 10.8a15.1 15.1 0 0 0 6.6 6.6l2.2-2.2a1 1 0 0 1 1-.25 11.4 11.4 0 0 0 3.6.57 1 1 0 0 1 1 1V20a1 1 0 0 1-1 1A17 17 0 0 1 3 4a1 1 0 0 1 1-1h3.5a1 1 0 0 1 1 1c0 1.25.2 2.45.57 3.57a1 1 0 0 1-.25 1z"/></svg>
          480-555-0172
        </li>
        <li>
          <svg width="12" height="10" viewBox="0 0 24 18" aria-hidden="true"><rect x="0" y="0" width="24" height="18" rx="2" fill="#3db843"/><path d="M1 2l11 8 11-8" fill="none" stroke="#f4f5f6" stroke-width="2"/></svg>
          glen@velmora-llc.example
        </li>
      </ul>
    </div>

    <div class="portrait" role="img" aria-label="Portrait photo of the home inspector in a navy company polo shirt"></div>
  </section>
</main>
</body>
</html>
```